Trulock Property Inspections

Property Inspection ( pre-purchase building inspections, swimming pool inspection, pest inspection , maintenance)

Industry/Entity Type

Building

Contact Information for Business Card

Omar Tanvelli
info@trulockinspections.com.au
0417 828 691

TruLock Property Inspections
www.trulockinspections.com.au

on the back

Property Inspections
Property Maintenance

Solid Home....Sure Family

```html
<!DOCTYPE html>
<html lang="en">
<head>
<meta charset="utf-8">
<title>Trulock Property Inspections – Business Card</title>
<link rel="stylesheet" href="https://fonts.googleapis.com/css2?family=Tinos:wght@400;700&display=swap">
<style>
  :root {
    --page: #ffffff;
    --silver-light: #f1f2f4;
    --silver-mid: #d6d8dc;
    --silver-dark: #a9acb2;
    --ink: #333333;
    --ink-soft: #3c3c3c;
    --accent-orange: #f07a22;
    --icon-blue: #1f6fc0;
  }
  * { margin: 0; padding: 0; box-sizing: border-box; }
  html, body {
    width: 1116px; height: 1200px; overflow: hidden;
    background: var(--page);
    font-family: "Tinos", "Times New Roman", serif;
  }
  .canvas { position: relative; width: 1116px; height: 1200px; }
  .card {
    position: absolute; left: 74px; width: 968px; height: 525px; overflow: hidden;
    background: linear-gradient(160deg, var(--silver-light) 0%, var(--silver-mid) 55%, var(--silver-dark) 100%);
  }
  .card--front { top: 64px; }
  .card--back { top: 610px; }
  .card__swoosh { position: absolute; inset: 0; width: 100%; height: 100%; }
  .brand {
    position: absolute; left: 70px; top: 110px; width: 320px;
    display: flex; align-items: center; gap: 12px;
  }
  .brand__mark { width: 26px; height: 26px; background: var(--icon-blue); flex: none; }
  .brand__name { font-size: 28px; font-weight: 700; color: var(--icon-blue); line-height: 1.15; }
  .person { position: absolute; left: 0; width: 454px; top: 292px; text-align: center; }
  .person__name { font-size: 45px; font-weight: 700; color: var(--accent-orange); line-height: 1; }
  .person__role { font-size: 27px; font-weight: 700; color: var(--ink); margin-top: 8px; }
  .contact { position: absolute; right: 42px; top: 248px; list-style: none; }
  .contact__item {
    display: flex; justify-content: flex-end; align-items: center; gap: 22px;
    height: 52px; font-size: 27px; color: var(--ink-soft);
  }
  .contact__item:nth-child(4) { margin-top: 4px; }
  .contact__icon { width: 46px; height: 46px; flex: none; }
  .tagline {
    position: absolute; left: 0; right: 0; top: 218px; text-align: center;
    font-size: 40px; font-weight: 700; color: var(--ink); line-height: 62px;
  }
</style>
</head>
<body>
<div class="canvas">
  <section class="card card--front">
    <svg class="card__swoosh" viewBox="0 0 968 525" preserveAspectRatio="none" aria-hidden="true">
      <defs>
        <linearGradient id="washFront" x1="0" y1="0" x2="1" y2="0">
          <stop offset="0" stop-color="#e4ebf5" stop-opacity="0.5"/>
          <stop offset="0.6" stop-color="#a9c6ea"/>
          <stop offset="1" stop-color="#5c93d6"/>
        </linearGradient>
      </defs>
      <path d="M0 0 H968 V130 C760 150 560 250 300 215 C180 200 80 230 0 250 Z" fill="url(#washFront)" opacity="0.75"/>
      <path d="M300 210 C560 245 760 140 968 95 V125 C760 160 560 260 300 215 Z" fill="#4f88d0" opacity="0.8"/>
      <path d="M420 180 C620 170 800 80 968 40 V0 H760 C700 60 580 150 420 180 Z" fill="#6f9fdc" opacity="0.5"/>
    </svg>
    <div class="brand">
      <span class="brand__mark"></span>
      <span class="brand__name">Trulock Property Inspections</span>
    </div>
    <div class="person">
      <p class="person__name">Omar Tanvelli</p>
      <p class="person__role">Director</p>
    </div>
    <ul class="contact">
      <li class="contact__item">TruLock Property Inspections
        <svg class="contact__icon" viewBox="0 0 46 46" aria-hidden="true"><circle cx="23" cy="23" r="21" fill="var(--icon-blue)"/><path d="M11 23 L23 12 L35 23 H31 V33 H15 V23 Z" fill="#fff"/><rect x="20" y="25" width="6" height="8" fill="var(--icon-blue)"/></svg>
      </li>
      <li class="contact__item">0417 828 691
        <svg class="contact__icon" viewBox="0 0 46 46" aria-hidden="true"><circle cx="23" cy="23" r="21" fill="var(--icon-blue)"/><path d="M11 20 Q23 10 35 20 L33 23 H28 V20 H18 V23 H13 Z" fill="#fff"/><rect x="14" y="25" width="18" height="9" rx="2" fill="#fff"/><circle cx="23" cy="29.5" r="2.5" fill="var(--icon-blue)"/></svg>
      </li>
      <li class="contact__item">info@trulockinspections.com.au
        <svg class="contact__icon" viewBox="0 0 46 46" aria-hidden="true"><circle cx="23" cy="23" r="21" fill="var(--icon-blue)"/><rect x="11" y="15" width="24" height="16" fill="#fff"/><path d="M11 15 L23 25 L35 15 M11 31 L20 22 M35 31 L26 22" stroke="var(--icon-blue)" stroke-width="1.8" fill="none"/></svg>
      </li>
      <li class="contact__item">www.trulockinspections.com.au
        <svg class="contact__icon" viewBox="0 0 46 46" aria-hidden="true"><circle cx="23" cy="23" r="21" fill="var(--icon-blue)"/><text x="23" y="31" text-anchor="middle" font-family="Tinos, serif" font-size="26" font-weight="700" fill="#fff">@</text></svg>
      </li>
    </ul>
  </section>

  <section class="card card--back">
    <svg class="card__swoosh" viewBox="0 0 968 525" preserveAspectRatio="none" aria-hidden="true">
      <defs>
        <linearGradient id="washBack" x1="0" y1="0" x2="1" y2="0">
          <stop offset="0" stop-color="#e6eef9" stop-opacity="0.9"/>
          <stop offset="0.6" stop-color="#a9c6ea"/>
          <stop offset="1" stop-color="#6b9dda"/>
        </linearGradient>
      </defs>
      <path d="M0 0 H968 V50 C760 100 520 180 260 205 C160 212 70 208 0 205 Z" fill="url(#washBack)" opacity="0.8"/>
      <path d="M0 200 C300 220 620 120 968 35 V50 C620 135 300 230 0 212 Z" fill="#5a8fd3" opacity="0.7"/>
    </svg>
    <p class="tagline">Property Inspections Property Maintenance<br>Solid Home....Sure Family</p>
  </section>
</div>
</body>
</html>
```